タイトル 「週末ガーデナーのための水やり流・花咲かせ節約術」
サブタイトル 「毎日が楽になる5つの習慣」

上記の表紙デザインをお願いします。基本お任せします。
本の内容  原稿を添付します。

その他ご不明な点がございましたらお気楽にご質問ください。よろしくお願いいたします。
著者名 星空ナビゲーター 森川佳代 from神戸

本の内容とよくマッチしたデザインだと思いました。インパクトもあり本の対象であるアラフォーの好みと合っているように思いました。

沢山のご応募ありがとうございました。何もかもか初めての作業で、不安でしたが、関心を持っていただいて心からありがたく思っております。これからも電子書籍の出版を考えております。ご縁がありましたらまた、今後もよろしくお願いします。
ありがとうございました。

```html
<!DOCTYPE html>
<html lang="ja">
<head>
<meta charset="utf-8">
<title>週末ガーデナーのための水やり流・花咲かせ節約術</title>
<link rel="stylesheet" href="https://fonts.googleapis.com/css2?family=Noto+Sans+JP:wght@400;700;900&family=Noto+Serif+JP:wght@500;700&display=swap">
<style>
  :root {
    --berry: #a83f6a;
    --gold: #c9a24a;
    --paper: #ffffff;
    --ink: #1c1c1c;
    --sun: #f5e21a;
  }
  html, body { margin: 0; padding: 0; overflow: hidden; background: var(--paper); }
  .cover {
    position: relative;
    width: 750px;
    height: 1200px;
    background: var(--paper);
    overflow: hidden;
    font-family: "Noto Sans JP", sans-serif;
  }
  .series {
    position: absolute;
    left: 0; right: 0;
    top: 196px;
    margin: 0;
    text-align: center;
    font-family: "Noto Serif JP", serif;
    font-weight: 500;
    font-size: 31px;
    letter-spacing: 0.14em;
    line-height: 50px;
    color: var(--ink);
  }
  .title-block {
    position: absolute;
    left: 246px;
    top: 300px;
    width: 258px;
    height: 258px;
    background: var(--berry);
  }
  .title-block .title {
    position: absolute;
    inset: 0;
    margin: 0;
    display: flex;
    flex-direction: row-reverse;
    justify-content: center;
    align-items: center;
    gap: 36px;
  }
  .title-block .title span {
    writing-mode: vertical-rl;
    font-family: "Noto Serif JP", serif;
    font-weight: 700;
    font-size: 46px;
    letter-spacing: 0.04em;
    color: var(--paper);
    line-height: 1;
  }
  .corner-accent {
    position: absolute;
    width: 18px;
    height: 18px;
    background: var(--gold);
  }
  .corner-accent.tl { left: 234px; top: 288px; }
  .corner-accent.tr { left: 498px; top: 288px; }
  .corner-accent.bl { left: 234px; top: 552px; }
  .corner-accent.br { left: 498px; top: 552px; }
  .author {
    position: absolute;
    left: 258px;
    top: 582px;
    color: var(--berry);
  }
  .author .label { font-size: 16px; font-weight: 700; display: block; line-height: 24px; }
  .author .role { font-size: 18px; font-weight: 700; display: block; line-height: 28px; }
  .author .name { font-size: 36px; font-weight: 700; letter-spacing: 0.04em; line-height: 48px; }
  .author .from { font-size: 17px; font-weight: 700; margin-left: 10px; }
  .band {
    position: absolute;
    left: 0; top: 738px;
    width: 750px; height: 462px;
    background: var(--berry);
  }
  .subtitle {
    position: absolute;
    left: 95px;
    top: 0;
    margin: 0;
    color: var(--paper);
  }
  .subtitle .num {
    position: absolute;
    left: 0;
    top: 42px;
    font-size: 170px;
    font-weight: 900;
    line-height: 1;
  }
  .subtitle .line {
    position: absolute;
    left: 108px;
    font-size: 42px;
    font-weight: 700;
    white-space: nowrap;
    letter-spacing: 0.06em;
    line-height: 1;
  }
  .subtitle .line.one { top: 66px; }
  .subtitle .line.two { top: 166px; }
  .lead {
    position: absolute;
    left: 0; right: 0;
    top: 268px;
    margin: 0;
    text-align: center;
    font-size: 35px;
    font-weight: 900;
    line-height: 62px;
    color: var(--ink);
  }
  .lead .light { color: var(--paper); }
  .lead .bright { color: var(--sun); }
</style>
</head>
<body>
<div class="cover">
  <p class="series">週末ガーデナーのための<br>水やり流</p>

  <div class="title-block">
    <h1 class="title"><span>花咲かせ</span><span>節約術</span></h1>
  </div>
  <div class="corner-accent tl" role="img" aria-label="金色の角飾り"></div>
  <div class="corner-accent tr" role="img" aria-label="金色の角飾り"></div>
  <div class="corner-accent bl" role="img" aria-label="金色の角飾り"></div>
  <div class="corner-accent br" role="img" aria-label="金色の角飾り"></div>

  <div class="author">
    <span class="label">著者</span>
    <span class="role">星空ナビゲーター</span>
    <span class="name">森川 佳代</span><span class="from">from神戸</span>
  </div>

  <section class="band">
    <h2 class="subtitle">
      <span class="num">5</span>
      <span class="line one">毎日が楽になる</span>
      <span class="line two">つの習慣</span>
    </h2>
    <p class="lead">
      忙しいあなた<span class="light">でも</span><br>
      <span class="bright">今日から“小さな庭”</span>を楽しめます<br>
      水やり<span class="light">のコツに気づいたなら…</span>
    </p>
  </section>
</div>
</body>
</html>
```